BrightHarbor is a fund management company that takes just four market positions a year. each position is linked to a big geopolitical and economic event happening in the world. So for example we may be buying gold mining stocks-these are the companies who dig the gold out of the ground, as all the gold is currently being bought by Asia, or buying the japanese stock market as this is one of the big stories of today.

I am looking for a logo that represents 'BrightHarbor'-the Bright Harbor.

I would like it to be small and sit to the left of the name of the company on the left hand side(I think!)on the top line of the business card please.

Industry/Entity Type

Mining

Contact Information for Business Card

BrightHarbor Investment management Ltd
41 Fennick Lane
London E9 7QT

Tomas P Hulme

Mob: 0(44)7839254086
Off: 0(44) 203 xxxx
email: th@brightharbor-fm.example

```html
<!DOCTYPE html>
<html lang="en">
<head>
<meta charset="utf-8">
<title>BrightHarbor Investment management Ltd – Business Card</title>
<link rel="stylesheet" href="https://fonts.googleapis.com/css2?family=Tinos&display=swap">
<style>
  :root {
    --card-bg: #ffffff;
    --ink-navy: #0b0b5c;
    --mark-orange: #ff7a00;
  }
  html, body {
    margin: 0;
    padding: 0;
    overflow: hidden;
  }
  .business-card {
    position: relative;
    width: 1200px;
    height: 800px;
    background: var(--card-bg);
    color: var(--ink-navy);
    font-family: "Tinos", "Times New Roman", serif;
    overflow: hidden;
  }
  .brand-mark {
    position: absolute;
    left: 110px;
    top: 150px;
    display: flex;
    align-items: center;
    gap: 18px;
  }
  .brand-dot {
    display: block;
    width: 84px;
    height: 84px;
    border-radius: 50%;
    background: var(--mark-orange);
  }
  .brand-name {
    font-size: 40px;
    line-height: 1;
    color: var(--ink-navy);
  }
  .company-name {
    position: absolute;
    left: 277px;
    top: 318px;
    margin: 0;
    font-size: 44px;
    font-weight: 400;
    line-height: 1.2;
    white-space: nowrap;
  }
  .contact-block {
    position: absolute;
    left: 110px;
    margin: 0;
    font-size: 31px;
    line-height: 40px;
    font-style: normal;
  }
  .contact-block p {
    margin: 0;
  }
  .address {
    top: 430px;
  }
  .person {
    top: 550px;
  }
</style>
</head>
<body>
  <main class="business-card">
    <div class="brand-mark">
      <span class="brand-dot" aria-hidden="true"></span>
      <span class="brand-name">BrightHarbor</span>
    </div>

    <h1 class="company-name">BrightHarbor Investment management Ltd</h1>

    <address class="contact-block address">
      <p>41 Fennick Lane</p>
      <p>London E9 7QT</p>
    </address>

    <address class="contact-block person">
      <p class="person-name">Tomas P Hulme</p>
      <p class="mobile">Mob: 0(44)7839254086</p>
      <p class="office">Off: 0(44) 203 xxxx</p>
      <p class="email">email: th@brightharbor-fm.example</p>
    </address>
  </main>
</body>
</html>
```